Stationary Design - KM Facial Plastics

We are looking for a stylish and professional stationary design for a facial plastic surgeon. The stationary design will be for letterhead, business card, appointment cards and envelopes.
The design must be slick and aesthetically pleasing whilst incorporating the style of our logo as attached below.

Target Market(s)

Adults of all ages

Font styles to use
Serif
Script

Requirements
Must have
• Must be an aesthetically pleasing, stylish and professional design that includes the required information in a captivating layout.
• Must also be welcoming with a balanced design and a clean crisp finish.
• Details should include:
• Mr Dorian Halvet - Consultant Otolaryngologist & Facial Plastic Surgeon
• Phone: 03 5917 2846
• Fax: 03 5918 4072
• Email: info@kmfacialplastics.example.au
• Consulting from: Bendigo, Echuca, Epping, Waverley & Melbourne CBD
• Appointment Card should include:
• Date, time, fee and location as per the attached example.
• location addresses are:
• 41 Marlow Street Echuca Vic 3564
• 318 Bramble Street Bendigo Vic 3550
• Level 3, 612 Hadley Street, Epping Vic 3076
• Level 6, 480 Tennant Street Melbourne Vic 3000
Should not have
• Clutter

```html
<!DOCTYPE html>
<html lang="en">
<head>
<meta charset="utf-8">
<title>KM Facial Plastics – Stationery Suite</title>
<link href="https://fonts.googleapis.com/css2?family=Cormorant+Garamond:wght@500&family=Arimo:wght@400;700&display=swap" rel="stylesheet">
<style>
  :root{
    --backdrop:#a9a9a9;
    --ink:#2b2a29;
    --ink-deep:#0f0e0e;
    --band-grey:#b9b9b9;
    --paper:#ffffff;
    --paper-shade:#e2e2e2;
    --text:#3a3a3a;
    --text-soft:#555;
    --mark-light:#d8d8d8;
  }
  *{margin:0;padding:0;box-sizing:border-box}
  html,body{width:1200px;height:991px;overflow:hidden}
  body{background:var(--backdrop);position:relative;font-family:"Arimo",Arial,sans-serif;color:var(--text)}
  a{color:inherit;text-decoration:none}
  .piece{position:absolute;background:var(--paper);box-shadow:0 1px 3px rgba(0,0,0,.3)}
  .piece svg{position:absolute;left:0;top:0}
  .brand{position:absolute;font-family:"Cormorant Garamond",Georgia,serif;font-weight:500;color:var(--ink);text-align:center;white-space:nowrap;transform:translateX(-50%)}
  .small-print{position:absolute;left:0;right:0;text-align:center;line-height:1.35;color:var(--text-soft)}

  .letterhead{left:168px;top:104px;width:397px;height:561px}
  .letterhead .brand{left:198px;top:56px;font-size:13px}
  .letterhead .web{top:508px;font-size:5px}
  .letterhead .rule{position:absolute;left:164px;width:70px;top:519px;border-top:.6px solid #888}
  .letterhead .contact{top:526px;font-size:5px}

  .folder{left:604px;top:90px;width:432px;height:575px;border-radius:5px;overflow:hidden}
  .folder .brand{left:216px;top:390px;font-size:18px}
  .folder .web{top:536px;font-size:8px;color:var(--text)}

  .card{top:326px;width:94px;height:170px}
  .card-front{left:118px}
  .card-back{left:232px}
  .card-front .brand{left:47px;top:36px;font-size:8px}
  .card-back .brand{left:47px;top:118px;font-size:8px}
  .card-front .holder{top:90px;font-size:5px;color:var(--ink);font-weight:700}
  .card-front .role{top:97px;font-size:3.2px}
  .card-front .phones{top:116px;font-size:3.2px}
  .card-front .addr{top:134px;font-size:3.2px}
  .card-front .site{top:148px;font-size:3.2px}

  .slip{left:168px;top:697px;width:415px;height:207px}
  .slip .brand{left:204px;top:66px;font-size:13px}
  .slip .addr{top:179px;font-size:5px}

  .envelope{left:613px;top:697px;width:415px;height:207px}
  .envelope .brand{left:207px;top:21px;font-size:6px;color:var(--mark-light)}
</style>
</head>
<body>

<section class="piece letterhead">
  <svg width="397" height="561" viewBox="0 0 397 561" aria-hidden="true">
    <rect width="397" height="50" fill="var(--ink)"/>
    <path d="M0 38 Q198 8 397 38 L397 60 L0 60Z" fill="var(--band-grey)"/>
    <circle cx="198" cy="64" r="54" fill="var(--band-grey)"/>
    <path d="M0 43 Q198 13 397 43 L397 561 L0 561Z" fill="var(--paper)"/>
    <circle cx="198" cy="64" r="51" fill="var(--paper)"/>
  </svg>
  <div class="brand">KM Facial Plastics</div>
  <p class="small-print web">www.coastalentclinic.example.au</p>
  <span class="rule"></span>
  <p class="small-print contact">318 Bramble Street, Marrowvale, Vic 3612<br>Tel: 03 5917 2846 · Fax: 03 5918 4072 · E: admin@coastalentclinic.example.au</p>
</section>

<section class="piece folder">
  <svg width="432" height="575" viewBox="0 0 432 575" aria-hidden="true">
    <defs>
      <linearGradient id="folderInk" x1="0" y1="0" x2="1" y2="0">
        <stop offset="0" stop-color="var(--ink)"/>
        <stop offset="1" stop-color="var(--ink-deep)"/>
      </linearGradient>
      <linearGradient id="folderPaper" gradientUnits="userSpaceOnUse" x1="120" y1="330" x2="432" y2="575">
        <stop offset="0.45" stop-color="#ffffff"/>
        <stop offset="1" stop-color="var(--paper-shade)"/>
      </linearGradient>
    </defs>
    <rect width="432" height="575" fill="url(#folderPaper)"/>
    <path d="M0 0 H432 V350 Q216 300 0 350Z" fill="url(#folderInk)"/>
    <path d="M0 350 Q216 300 432 350 L432 366 Q216 316 0 366Z" fill="var(--band-grey)"/>
    <circle cx="216" cy="400" r="76" fill="var(--band-grey)"/>
    <path d="M0 364 Q216 314 432 364 V575 H0Z" fill="url(#folderPaper)"/>
    <circle cx="216" cy="400" r="72" fill="url(#folderPaper)"/>
  </svg>
  <div class="brand">KM Facial Plastics</div>
  <p class="small-print web">www.coastalentclinic.example.au</p>
</section>

<section class="piece card card-front">
  <svg width="94" height="170" viewBox="0 0 94 170" aria-hidden="true">
    <rect width="94" height="18" fill="var(--ink)"/>
    <path d="M0 14 Q47 6 94 14 L94 24 L0 24Z" fill="var(--band-grey)"/>
    <circle cx="47" cy="40" r="27" fill="var(--band-grey)"/>
    <path d="M0 19 Q47 11 94 19 L94 170 L0 170Z" fill="var(--paper)"/>
    <circle cx="47" cy="40" r="25" fill="var(--paper)"/>
  </svg>
  <div class="brand">KM Facial Plastics</div>
  <p class="small-print holder">Mr Dorian Halvet</p>
  <p class="small-print role">Consultant Otolaryngologist<br>&amp; Facial Plastic Surgeon</p>
  <p class="small-print phones">T: 03 5917 2846<br>F: 03 5918 4072<br>E: admin@coastalentclinic.example.au</p>
  <p class="small-print addr">318 Bramble Street<br>Marrowvale, Vic 3612</p>
  <p class="small-print site">www.coastalentclinic.example.au</p>
</section>

<section class="piece card card-back">
  <svg width="94" height="170" viewBox="0 0 94 170" aria-hidden="true">
    <rect width="94" height="104" fill="var(--ink)"/>
    <path d="M0 98 Q47 90 94 98 L94 110 L0 110Z" fill="var(--band-grey)"/>
    <circle cx="47" cy="122" r="27" fill="var(--band-grey)"/>
    <path d="M0 103 Q47 95 94 103 L94 170 L0 170Z" fill="var(--paper)"/>
    <circle cx="47" cy="122" r="25" fill="var(--paper)"/>
  </svg>
  <div class="brand">KM Facial Plastics</div>
</section>

<section class="piece slip">
  <svg width="415" height="207" viewBox="0 0 415 207" aria-hidden="true">
    <rect width="415" height="50" fill="var(--ink)"/>
    <path d="M0 47 Q204 16 415 47 L415 60 L0 60Z" fill="var(--band-grey)"/>
    <circle cx="204" cy="71" r="56" fill="var(--band-grey)"/>
    <path d="M0 53 Q204 22 415 53 L415 207 L0 207Z" fill="var(--paper)"/>
    <circle cx="204" cy="71" r="53" fill="var(--paper)"/>
  </svg>
  <div class="brand">KM Facial Plastics</div>
  <p class="small-print addr">318 Bramble Street<br>Marrowvale, Vic 3612</p>
</section>

<section class="piece envelope">
  <svg width="415" height="207" viewBox="0 0 415 207" aria-hidden="true">
    <path d="M5 0 H410 V38 Q410 53 395 53 H20 Q5 53 5 38Z" fill="var(--ink)"/>
  </svg>
  <div class="brand">KM Facial Plastics</div>
</section>

</body>
</html>
```